Retractable Banner Stands

Hello we need a deisgn for a banner.
Sizes: 36"x80", 12"x17"(this one to have less on it, most the logo, license numvber, and address), and a 24"x40" banner
Roofing Services
HOA & Commercial Roofing
• Emergency roof tarping & repairs — Starting at $550
• Small & large roof repairs
• Preventative roof maintenance
• Full roof replacement
Deck & Balcony Services
• Balcony & deck maintenance
SB-326 Repairs
• Deck resurfacing
• Small & large deck repairs
• Full deck reconstruction
Gutter Services
• Small & large gutter repairs
• Gutter cleaning & maintenance
• New gutter installation & replacement
License Information:
C-39 Roofing Contractor
General B Contractor
License #4529730
📍 Serving Orange County & Surrounding Areas
📍 Office Location:
41 Dunwick Street, Suite F
Target Market(s)
HOA & Commerical roofs
Industry/Entity Type
Roofing
Other font styles liked:
- Gotham
Look and feel

```html
<!DOCTYPE html>
<html lang="en">
<head>
<meta charset="utf-8">
<title>Crestline Roofing &amp; Waterproofing – Banner</title>
<link href="https://fonts.googleapis.com/css2?family=Fredoka:wght@400;500;600&display=swap" rel="stylesheet">
<style>
  :root{
    --brand-blue:#3571ee;
    --text-blue:#1f68e4;
    --ink:#141414;
    --white:#ffffff;
    --pin-yellow:#f2c21b;
    --photo-warm:#d9a56a;
    --photo-sky:#9fc8e8;
    --photo-steel:#4d6f9c;
  }
  *{margin:0;padding:0;box-sizing:border-box}
  html,body{width:847px;height:1200px;overflow:hidden;background:var(--white)}
  .banner{position:relative;width:847px;height:1200px;overflow:hidden;font-family:"Fredoka",sans-serif;background:var(--white)}
  .backdrop{position:absolute;inset:0}
  .abs{position:absolute;line-height:1;white-space:nowrap}

  .brand-name{left:90px;top:52px;font-size:74px;font-weight:600;color:var(--white);letter-spacing:1px}
  .brand-sub{left:39px;top:163px;font-size:25px;font-weight:500;color:var(--white);letter-spacing:.5px}

  .license{left:528px;top:33px;color:var(--white);font-size:21px;font-weight:500}
  .license p{line-height:30px}
  .license .license-title{font-weight:600}

  .tagline{left:395px;width:452px;top:282px;text-align:center;color:var(--text-blue);font-size:23px;font-weight:600;line-height:32px;white-space:normal}

  .services-title{left:358px;top:373px;font-size:28px;font-weight:500;color:var(--text-blue)}
  .service-group{position:absolute;left:358px;color:var(--text-blue)}
  .service-group h3{font-size:15.5px;font-weight:600;line-height:1;margin-bottom:19px}
  .service-group ul{list-style:none}
  .service-group li{font-size:14.8px;font-weight:500;line-height:21.5px}
  .service-group li::before{content:"\2022";margin-right:4px}
  .group-roofing{top:432px}
  .group-deck{top:603px}
  .group-gutter{top:775px}

  .contact-title,.office-title{left:357px;font-size:30px;font-weight:500;color:var(--ink)}
  .contact-title{top:917px}
  .office-title{top:1005px}
  .icon{position:absolute;left:360px;width:28px;height:28px}
  .icon-phone{top:957px}
  .icon-pin{top:1052px}
  .phone{left:411px;top:957px;font-size:28px;font-weight:500;color:var(--ink)}
  .address{left:407px;top:1042px;font-size:28px;font-weight:500;color:var(--ink)}
  .address p{line-height:42.5px}
</style>
</head>
<body>
<div class="banner">
  <svg class="backdrop" width="847" height="1200" viewBox="0 0 1200 1700" preserveAspectRatio="none" aria-hidden="false">
    <polygon points="0,0 1200,0 1200,205 447,395 447,1700 0,1700" fill="var(--brand-blue)"/>
    <g role="img" aria-label="Photo: roofer in hard hat hammering on a roof">
      <polygon points="0,505 447,395 447,742 0,855" fill="var(--photo-warm)"/>
    </g>
    <g role="img" aria-label="Photo: worker in safety vest fastening a metal roof panel">
      <polygon points="0,860 447,748 447,1118 0,1225" fill="var(--photo-steel)"/>
    </g>
    <g role="img" aria-label="Photo: roofer hammering against a blue sky">
      <polygon points="0,1230 447,1124 447,1500 0,1555" fill="var(--photo-sky)"/>
    </g>
  </svg>

  <div class="abs brand-name">CRESTLINE</div>
  <div class="abs brand-sub">ROOFING &amp; WATERPROOFING</div>

  <div class="abs license">
    <p class="license-title">LICENSE INFORMATION:</p>
    <p>C-39 Roofing Contractor</p>
    <p>General B Contractor</p>
    <p>License #4529730</p>
  </div>

  <div class="abs tagline">WE ARE EXPERT<br>IN ROOFING &amp; WATERPROOFING</div>

  <h2 class="abs services-title">OUR SERVICES</h2>

  <section class="service-group group-roofing">
    <h3>HOA &amp; COMMERCIAL ROOFING</h3>
    <ul>
      <li>Emergency Roof Tarping &amp; Repairs — Starting at $550</li>
      <li>Small &amp; Large Roof Repairs</li>
      <li>Preventative Roof Maintenance</li>
      <li>Full Roof Replacement</li>
    </ul>
  </section>

  <section class="service-group group-deck">
    <h3>DECK &amp; BALCONY SERVICES</h3>
    <ul>
      <li>Balcony &amp; Deck Maintenance SB-326 Repairs</li>
      <li>Deck Resurfacing</li>
      <li>Small &amp; Large Deck Repairs</li>
      <li>Full Deck Reconstruction</li>
    </ul>
  </section>

  <section class="service-group group-gutter">
    <h3>GUTTER SERVICES</h3>
    <ul>
      <li>Small &amp; Large Gutter Repairs</li>
      <li>Gutter Cleaning &amp; Maintenance</li>
      <li>New Gutter Installation &amp; Replacement</li>
    </ul>
  </section>

  <div class="abs contact-title">Contact Us:</div>
  <svg class="icon icon-phone" viewBox="0 0 28 28" aria-label="Phone">
    <rect width="28" height="26" fill="var(--brand-blue)"/>
    <path d="M9 6 l3 0 l1.5 4 l-2 1.5 a10 10 0 0 0 5 5 l1.5 -2 l4 1.5 l0 3 a2 2 0 0 1 -2 2 a15 15 0 0 1 -13 -13 a2 2 0 0 1 2 -2z" fill="var(--pin-yellow)"/>
  </svg>
  <div class="abs phone">1-800-2739</div>

  <div class="abs office-title">Office Location:</div>
  <svg class="icon icon-pin" viewBox="0 0 28 28" aria-label="Location">
    <rect width="28" height="28" fill="var(--brand-blue)"/>
    <path d="M14 4 a7 7 0 0 1 7 7 c0 5 -7 12 -7 12 s-7 -7 -7 -12 a7 7 0 0 1 7 -7z" fill="var(--pin-yellow)"/>
    <circle cx="14" cy="11" r="2.8" fill="var(--brand-blue)"/>
  </svg>
  <div class="abs address">
    <p>41 Dunwick Street, Suite F</p>
    <p>Serving Orange County</p>
    <p>&amp; Surrounding Areas</p>
  </div>
</div>
</body>
</html>
```